Tembo & Lusani Advocates website

An interactive professional law firm website fully synchronized with social media pages.

Target Market(s)

Corporations and professionals

Industry/Entity Type

Professional Service

Number of Pages Required

5+ page

Font styles to use
Sans Serif

Colors

Designer to choose colors to be used in the design.

```html
<!DOCTYPE html>
<html lang="en">
<head>
<meta charset="utf-8">
<title>Tembo &amp; Lusani Advocates</title>
<link rel="stylesheet" href="https://fonts.googleapis.com/css2?family=Libre+Baskerville&family=Montserrat:wght@400;600;700&family=Open+Sans:wght@400;600;700&display=swap">
<style>
:root{
  --red:#9e1b22;
  --maroon:#861a23;
  --bright:#c41820;
  --dark:#2b2f36;
  --navy:#1f2a3a;
  --grey:#ececec;
  --salmon:#f0605a;
  --ink:#222;
  --white:#fff;
}
*{box-sizing:border-box;margin:0;padding:0}
html,body{width:1200px;height:3805px;overflow:hidden}
body{font-family:"Open Sans",sans-serif;color:var(--ink);background:var(--white);position:relative}
section,header,footer,nav{position:absolute;left:0;width:1200px}
.wrap{position:absolute;left:114px;width:972px}
h2.section-title{font-family:"Montserrat",sans-serif;font-weight:600;font-size:26px;letter-spacing:2px;text-align:center;position:absolute;left:0;width:1200px}
h2.section-title::after{content:"";display:block;width:50px;height:3px;background:var(--bright);margin:10px auto 0}

/* top bar */
.topbar{top:0;height:30px;background:var(--red);color:#fff;font-size:11px;font-weight:600;letter-spacing:.3px}
.topbar .office{position:absolute;left:90px;top:8px}
.topbar .contacts{position:absolute;right:90px;top:8px;display:flex;gap:38px;align-items:center}
.topbar svg{vertical-align:-2px;margin-right:6px}

/* header */
.masthead{top:30px;height:160px;background:#fbfbfd;text-align:center}
.brand{position:absolute;left:0;width:1200px;top:34px;display:flex;justify-content:center;align-items:center;gap:16px}
.brand-square{width:46px;height:46px;background:var(--red)}
.brand-name{font-family:"Libre Baskerville",serif;font-size:34px;color:#5a5a5a;line-height:1}
.tagline{position:absolute;left:0;width:1200px;top:118px;font-family:"Montserrat",sans-serif;font-size:10px;letter-spacing:3px;color:var(--red)}
.tagline span{margin:0 10px;color:#999}

/* nav */
.mainnav{top:190px;height:51px;background:var(--red)}
.mainnav ul{list-style:none;display:flex;position:absolute;left:107px;top:0;height:51px}
.mainnav li{font-family:"Montserrat",sans-serif;font-size:12px;color:#fff;padding:0 18px;line-height:51px;font-weight:600}
.mainnav li.active{background:var(--navy)}

/* hero */
.hero{top:241px;height:464px;background:linear-gradient(180deg,#1a2230 0%,#2f3645 45%,#5b4a3b 75%,#2a2420 100%)}
.hero h1{position:absolute;top:150px;left:0;width:1200px;text-align:center;font-family:"Libre Baskerville",serif;font-weight:400;font-size:46px;color:#fff;letter-spacing:1px}
.hero p{position:absolute;top:246px;left:300px;width:600px;text-align:center;color:#eee;font-size:15px;line-height:1.6}
.hero .btn{position:absolute;top:353px;left:458px;width:228px;height:34px;border:1px solid #fff;color:#fff;font-size:11px;letter-spacing:2px;text-align:center;line-height:32px;font-family:"Montserrat",sans-serif}
.dots{position:absolute;top:415px;left:0;width:1200px;display:flex;justify-content:center;gap:9px}
.dots i{width:10px;height:10px;border-radius:50%;background:var(--bright)}
.dots i:first-child{background:#fff}

/* about */
.about{top:705px;height:538px;background:linear-gradient(180deg,#8e1c26,#7d1821)}
.about .text{position:absolute;left:96px;top:86px;width:410px;color:#fff}
.about h3{font-family:"Montserrat",sans-serif;font-size:23px;font-weight:600;letter-spacing:1px;margin-bottom:16px}
.about p{font-size:14px;line-height:1.6;margin-bottom:40px}
.team-frame{position:absolute;left:578px;top:100px;width:470px;height:330px;background:#fff;transform:rotate(-1.5deg)}
.team-photo{position:absolute;left:588px;top:108px;width:450px;height:314px;background:linear-gradient(160deg,#6d6a6c,#2e2b2f 60%,#8a2a2e)}

/* practice */
.practice{top:1243px;height:368px;background:linear-gradient(180deg,rgba(110,20,30,.85),rgba(60,22,34,.9)),linear-gradient(90deg,#3b3446,#2a2635)}
.practice h2{top:42px;color:#fff}
.cards{position:absolute;left:114px;top:127px;display:flex;gap:32px}
.card{width:206px;height:165px;background:#fff;position:relative}
.card svg{position:absolute;left:83px;top:40px}
.card .label{position:absolute;left:0;bottom:0;width:100%;height:42px;background:var(--maroon);color:#fff;font-family:"Montserrat",sans-serif;font-weight:600;font-size:11px;text-align:center;line-height:42px}

/* method */
.method{top:1611px;height:414px;background:linear-gradient(180deg,#2c3139,#3a3f46 60%,#262a30)}
.method h2{top:36px;color:#fff}
.value{position:absolute;left:170px;width:860px;text-align:center;color:#fff}
.value h4{font-family:"Montserrat",sans-serif;color:#e0272d;font-size:17px;letter-spacing:3px;font-weight:700;margin-bottom:8px}
.value p{font-size:12px;line-height:1.8}

/* attorneys */
.attorneys{top:2025px;height:499px;background:var(--grey)}
.attorneys h2{top:38px;color:#222}
.team{position:absolute;left:117px;top:126px;display:flex;gap:22px}
.lawyer{width:214px;height:310px;position:relative}
.lawyer .portrait{height:226px;background:linear-gradient(180deg,#3c5a75,#1d2836 70%,#151b24)}
.lawyer .name{height:84px;background:var(--maroon);color:#fff;text-align:center;padding-top:18px}
.lawyer strong{display:block;font-family:"Montserrat",sans-serif;font-size:12px;font-weight:700;letter-spacing:.5px}
.lawyer span{font-size:11px;line-height:1.4;display:block;margin-top:4px}
.arrow{position:absolute;width:40px;height:40px;border-radius:50%;display:flex;align-items:center;justify-content:center}
.arrow.red{background:var(--maroon)}
.arrow.white{background:#fff;width:32px;height:32px}

/* clients */
.clients{top:2524px;height:356px;background:linear-gradient(180deg,#b52a34,#c0474c 60%,#b8383f)}
.clients h2{top:42px;color:#fff}
.logos{position:absolute;left:124px;top:140px;display:flex;gap:22px}
.client{width:164px;height:129px;background:#fff;display:flex;align-items:center;justify-content:center;gap:8px;box-shadow:0 2px 6px rgba(0,0,0,.2)}
.client i{width:14px;height:14px;background:var(--bright);display:block}
.client b{font-family:"Open Sans",sans-serif;font-weight:700;font-size:17px;color:var(--maroon)}

/* features */
.features{top:2880px;height:464px;background:linear-gradient(180deg,rgba(40,45,55,.82),rgba(40,45,55,.88)),linear-gradient(120deg,#6f6c68,#3a3d44)}
.features h2{top:72px;color:#fff}
.feats{position:absolute;left:114px;top:164px;width:972px;display:flex;justify-content:space-around}
.feat{width:200px;text-align:center;color:#fff}
.feat .ring{width:122px;height:122px;border-radius:50%;background:#c8171f;margin:0 auto 18px;display:flex;align-items:center;justify-content:center}
.feat span{font-family:"Montserrat",sans-serif;font-size:12px;letter-spacing:1.5px;line-height:1.6}

/* footer */
.footer{top:3344px;height:398px;background:#2a2a2a}
.info{position:absolute;left:96px;top:24px;color:#fff;font-size:11.5px;line-height:1.55}
.info h5{font-family:"Montserrat",sans-serif;font-size:13px;margin-bottom:6px}
.info em{display:block;color:#e0272d;font-style:normal;font-weight:600;margin-top:14px}
.social{display:flex;gap:6px;margin-top:14px}
.social i{width:24px;height:24px;background:#3b78c9;display:block}
.contact-form{position:absolute;left:426px;top:0;width:302px;height:398px;background:var(--salmon);padding:22px 24px;color:#fff}
.contact-form h3{font-family:"Montserrat",sans-serif;font-weight:400;font-size:26px;letter-spacing:1px;margin-bottom:20px}
.field{font-size:11px;border-bottom:1px solid rgba(255,255,255,.7);height:40px;padding-top:14px}
.field.msg{height:96px}
.submit{margin:30px auto 0;width:180px;height:46px;background:#fff;color:#c0161e;font-family:"Montserrat",sans-serif;font-weight:600;font-size:14px;text-align:center;line-height:46px}
.map{position:absolute;left:728px;top:0;width:472px;height:398px;background:linear-gradient(135deg,#e4e4e4,#cfcfcf 50%,#dedede)}
.legal{top:3742px;height:63px;background:#1e1e1e;color:#ddd;font-size:11px;text-align:center;padding-top:14px;line-height:1.6}
</style>
</head>
<body>

<div class="topbar">
  <div class="office">OFFICES: PLOT 14, ACACIA ROAD, KAMPALA, UGANDA</div>
  <div class="contacts">
    <span><svg width="14" height="10" viewBox="0 0 14 10"><rect x=".5" y=".5" width="13" height="9" fill="none" stroke="#fff"/><path d="M1 1l6 5 6-5" fill="none" stroke="#fff"/></svg>INFO@TEMBOLUSANI.COM</span>
    <span><svg width="12" height="12" viewBox="0 0 24 24"><path fill="#fff" d="M6.6 10.8a15 15 0 006.6 6.6l2.2-2.2c.3-.3.7-.4 1-.2 1.1.4 2.3.6 3.6.6.6 0 1 .4 1 1V20c0 .6-.4 1-1 1A17 17 0 013 4c0-.6.4-1 1-1h3.5c.6 0 1 .4 1 1 0 1.3.2 2.5.6 3.6.1.3 0 .7-.2 1z"/></svg>0400 123 456</span>
  </div>
</div>

<header class="masthead">
  <div class="brand"><div class="brand-square"></div><div class="brand-name">Tembo &amp; Lusani Advocates</div></div>
  <div class="tagline">CONSTRUCTION LAW<span>|</span>ARBITRATION<span>|</span>LITIGATION</div>
</header>

<nav class="mainnav">
  <ul>
    <li class="active">HOME</li><li>OUR HISTORY</li><li>WHO WE ARE</li><li>PRACTICE AREAS</li><li>HOW WE DO IT</li><li>OUR CLIENTS</li><li>OUR PROFESSIONALS</li><li>CONTACT US</li>
  </ul>
</nav>

<section class="hero" role="img" aria-label="Night view of a city skyline with lit office towers">
  <h1>LOREM IPSUM DOLOR SIT AMET</h1>
  <p>Aenean imperdiet ante id nisi dapibus sodales. Aenean ex velit, dictum vitae lacus non, accumsan euismod erat. Pellentesque lacinia ex pulvinar eleifend eu, mollis erat vivamus sed sagittis neque.</p>
  <div class="btn">KNOW MORE</div>
  <div class="dots"><i></i><i></i><i></i><i></i><i></i></div>
</section>

<section class="about">
  <div class="text">
    <h3>WHO WE ARE?</h3>
    <p>Tembo &amp; Lusani Advocates are a specialist commercial law firm in Uganda focusing on commercial litigation.</p>
    <h3>MISSION</h3>
    <p>To be the firm of choice in our niche practice areas of commercial law.</p>
    <h3>VISION</h3>
    <p>To provide legal services focused on commercial litigation, construction law and arbitration with efficiency, integrity and client satisfaction.</p>
  </div>
  <div class="team-frame"></div>
  <div class="team-photo" role="img" aria-label="Group photograph of the firm's advocates standing together in an office"></div>
</section>

<section class="practice">
  <h2 class="section-title">OUR PRACTICE AREA</h2>
  <div class="cards">
    <div class="card"><svg width="40" height="40" viewBox="0 0 40 40" fill="none" stroke="#c41820" stroke-width="2.5"><path d="M5 20L20 7l15 13"/><path d="M10 16v17h20V16"/><rect x="16" y="23" width="8" height="10"/></svg><div class="label">CONSTRUCTION LAW</div></div>
    <div class="card"><svg width="40" height="40" viewBox="0 0 40 40" fill="none" stroke="#c41820" stroke-width="2.5"><path d="M10 14l10-10 6 6-10 10z"/><path d="M19 17l14 14"/><path d="M6 36h16"/></svg><div class="label">COMMERCIAL LITIGATION</div></div>
    <div class="card"><svg width="40" height="40" viewBox="0 0 40 40" fill="none" stroke="#c41820" stroke-width="2.5"><circle cx="13" cy="9" r="4"/><circle cx="27" cy="9" r="4"/><path d="M8 36V18h10v18M22 36V18h10v18M18 24h4"/></svg><div class="label">ARBITRATION</div></div>
    <div class="card"><svg width="40" height="40" viewBox="0 0 40 40" fill="none" stroke="#c41820" stroke-width="2.5"><path d="M4 4l6 6M10 4l-6 6M30 30l6 6M36 30l-6 6"/><circle cx="32" cy="8" r="4"/><circle cx="8" cy="32" r="4"/><path d="M10 14c4 10 10 14 18 16" stroke-dasharray="3 3"/></svg><div class="label">CORPORATE ADVISORY</div></div>
  </div>
</section>

<section class="method">
  <h2 class="section-title">HOW WE DO IT?</h2>
  <div class="value" style="top:118px"><h4>INTEGRITY</h4><p>We partner with our clients and keep a close and interactive relationship that enriches our business knowledge and allows us to provide strategic,<br>innovative and forward thinking solutions fit to meet the challenges they face every day.</p></div>
  <div class="value" style="top:216px"><h4>PARTNERSHIP</h4><p>We work to surpass our clients' expectations. We are practical and solution-driven in our approach. We are innovative and creative, and we focus<br>sharply and firmly on the issues we undertake.</p></div>
  <div class="value" style="top:314px"><h4>EFFICIENCY</h4><p>We work to surpass our clients' expectations. We are practical and solution-driven in our approach. We are innovative and creative, and we focus<br>sharply and firmly on the issues we undertake.</p></div>
</section>

<section class="attorneys">
  <h2 class="section-title">OUR ATTORNEYS</h2>
  <div class="arrow red" style="left:38px;top:261px"><svg width="12" height="14" viewBox="0 0 12 14"><path d="M9 1L3 7l6 6" fill="none" stroke="#fff" stroke-width="3"/></svg></div>
  <div class="team">
    <div class="lawyer"><div class="portrait" role="img" aria-label="Portrait of the managing partner"></div><div class="name"><strong>PETER M. TEMBO</strong><span>Managing Partner</span></div></div>
    <div class="lawyer"><div class="portrait" role="img" aria-label="Portrait of the senior partner"></div><div class="name"><strong>DANIEL R. LUSANI</strong><span>Senior Partner</span></div></div>
    <div class="lawyer"><div class="portrait" role="img" aria-label="Portrait of the head of litigation"></div><div class="name"><strong>SIMON ADEKE</strong><span>Partner( Head of Litigation)</span></div></div>
    <div class="lawyer"><div class="portrait" role="img" aria-label="Portrait of the head of business developments"></div><div class="name"><strong>Nathan Kirabo</strong><span>Partner ( Head of<br>Business Developments)</span></div></div>
  </div>
  <div class="arrow red" style="left:1071px;top:261px"><svg width="12" height="14" viewBox="0 0 12 14"><path d="M3 1l6 6-6 6" fill="none" stroke="#fff" stroke-width="3"/></svg></div>
</section>

<section class="clients">
  <h2 class="section-title">OUR HAPPY CLIENTS</h2>
  <div class="arrow white" style="left:48px;top:188px"><svg width="10" height="12" viewBox="0 0 10 12"><path d="M7 1L2 6l5 5" fill="none" stroke="#333" stroke-width="2"/></svg></div>
  <div class="logos">
    <div class="client"><i></i><b>Revenue Board</b></div>
    <div class="client"><b>Bright Path</b></div>
    <div class="client"><b>Unity Assurance</b></div>
    <div class="client"><b>Kora Build</b></div>
    <div class="client"><b>Meridian Group</b></div>
  </div>
  <div class="arrow white" style="left:1070px;top:188px"><svg width="10" height="12" viewBox="0 0 10 12"><path d="M3 1l5 5-5 5" fill="none" stroke="#333" stroke-width="2"/></svg></div>
</section>

<section class="features">
  <h2 class="section-title">FEATURES</h2>
  <div class="arrow white" style="left:48px;top:230px"><svg width="10" height="12" viewBox="0 0 10 12"><path d="M7 1L2 6l5 5" fill="none" stroke="#333" stroke-width="2"/></svg></div>
  <div class="feats">
    <div class="feat"><div class="ring"><svg width="54" height="54" viewBox="0 0 54 54" fill="none" stroke="#fff" stroke-width="3"><path d="M6 22l12-10 9 7 9-7 12 10-10 12-11-9-11 9z"/><path d="M20 36l6 6M26 32l8 8M32 30l6 6"/></svg></div><span>5 PARTNERS</span></div>
    <div class="feat"><div class="ring"><svg width="54" height="54" viewBox="0 0 54 54" fill="#fff"><circle cx="27" cy="14" r="6"/><circle cx="13" cy="19" r="5"/><circle cx="41" cy="19" r="5"/><rect x="21" y="22" width="12" height="20" rx="3"/><rect x="8" y="26" width="10" height="16" rx="3"/><rect x="36" y="26" width="10" height="16" rx="3"/></svg></div><span>20+ PEOPLE</span></div>
    <div class="feat"><div class="ring"><svg width="54" height="54" viewBox="0 0 54 54" fill="none" stroke="#fff" stroke-width="3"><rect x="9" y="12" width="36" height="32" rx="3"/><path d="M9 21h36M18 7v9M36 7v9"/><circle cx="27" cy="32" r="7"/><path d="M27 28v4l3 2"/></svg></div><span>55 YEARS OF<br>COMBINED EXPERIENCE</span></div>
    <div class="feat"><div class="ring"><svg width="54" height="54" viewBox="0 0 54 54" fill="#fff"><rect x="10" y="34" width="7" height="10"/><rect x="21" y="28" width="7" height="16"/><rect x="32" y="22" width="7" height="22"/><path d="M10 26l12-10 8 6 12-12" stroke="#fff" stroke-width="3" fill="none"/><path d="M36 9h8v8z"/></svg></div><span>350+ CASE SOLVED</span></div>
  </div>
  <div class="arrow white" style="left:1070px;top:230px"><svg width="10" height="12" viewBox="0 0 10 12"><path d="M3 1l5 5-5 5" fill="none" stroke="#333" stroke-width="2"/></svg></div>
</section>

<footer class="footer">
  <div class="info">
    <h5>KAMPALA, UGANDA</h5>
    <em style="margin-top:0">Find Us</em>
    Plot 14, Acacia Road 2nd Floor, Amani House<br>P.O Box 4410, Kampala, Uganda
    <em>Call Us Today</em>
    T: 0400 123 456<br>M: +256 (0) 700 555 218
    <em>Email Us Now</em>
    info@tembolusani.com
    <em>Visit Our Website</em>
    www.tembolusani.com
    <div class="social"><i></i><i></i><i style="background:#d9443a"></i><i style="background:#2d7bb6"></i></div>
  </div>
  <div class="contact-form">
    <h3>CONTACT US</h3>
    <div class="field">Name</div>
    <div class="field">Email</div>
    <div class="field">Phone</div>
    <div class="field msg">Message</div>
    <div class="submit">SUBMIT</div>
  </div>
  <div class="map" role="img" aria-label="Street map showing the office location"></div>
</footer>

<div class="legal" style="position:absolute;left:0;width:1200px">© 2018,©Tembo &amp; Lusani- All rights reserved. Tembo &amp; Lusani is the trading name of Tembo &amp; Lusani, which is authorised and regulated by the<br>Solicitors Regulation Authority (SRA Number 600418). VAT Number: 100 2233 45</div>

</body>
</html>
```